Generic fund comparison

We need a power point template to be used for presentation decks and proposals to clients and prospects. We are an independent Registered Investment Advisor in Pittsburgh Pennsylvania.
Our services include family office, alternative investments, investment management, financial planning and consulting.
We would like to see designs that use the color green and grey as they are part of our logo and brand image. The final design should communicate our guiding principles: 'educate, plan, implement, adapt'

```html
<!DOCTYPE html>
<html lang="en">
<head>
<meta charset="utf-8">
<title>Tessera – Presentation Template</title>
<link href="https://fonts.googleapis.com/css2?family=Roboto:wght@400;500;700;900&display=swap" rel="stylesheet">
<style>
:root{
  --green:#86c232;
  --grey:#6a6866;
  --ink:#161616;
  --body:#5a5a5a;
  --rule:#cfcfcf;
  --page:#ececec;
  --photo-a:#8e8e8e;
  --photo-b:#d4d4d4;
}
*{margin:0;padding:0;box-sizing:border-box}
html,body{width:1200px;height:4310px;overflow:hidden;background:var(--page);font-family:'Roboto',Arial,sans-serif;color:var(--ink)}
.slide{position:absolute;left:44px;width:1108px;height:623px;background:#fff;overflow:hidden}
.slide.framed{border-bottom:3px solid var(--green)}
.brand{position:absolute;display:flex;flex-direction:column;align-items:center;gap:8px}
.brand-square{width:25px;height:25px;background:var(--green)}
.brand-name{font-family:'Roboto',Arial,sans-serif;font-weight:500;font-size:16px;letter-spacing:2px;color:var(--grey)}
.slide .brand.corner{right:50px;top:20px}
.page-num{position:absolute;right:34px;bottom:16px;display:flex;align-items:center}
.page-num .num{width:26px;height:26px;border-radius:50%;background:var(--green);color:#fff;font-size:12px;display:flex;align-items:center;justify-content:center;position:relative;z-index:1}
.page-num .dot{width:26px;height:26px;border-radius:50%;background:var(--grey);margin-left:-10px}
.photo{position:absolute;background:linear-gradient(160deg,var(--photo-a),var(--photo-b) 55%,#a3a3a3)}
/* cover & closing */
.cover .photo{left:0;top:0;width:1108px;height:397px;border-bottom:6px solid #fff}
.hero-brand{position:absolute;left:0;right:0;top:90px;display:flex;flex-direction:column;align-items:center;gap:18px}
.hero-brand .brand-square{width:77px;height:77px}
.hero-brand .brand-name{font-size:50px;color:#fff;letter-spacing:6px;font-weight:500}
.cover-band{position:absolute;left:0;top:405px;width:1108px;height:218px;background:var(--green);color:#fff;text-align:center;font-weight:700}
.cover-band .headline{font-size:24px;margin-top:66px}
.cover-band .sub{font-size:24px;margin-top:28px}
.closing-band{position:absolute;left:0;top:403px;width:1108px;height:220px;background:var(--grey);border-top:3px solid var(--green);color:#fff;text-align:center}
.closing-band .headline{font-size:24px;font-weight:700;margin-top:68px}
.social{display:flex;justify-content:center;gap:14px;margin-top:22px}
.social span{width:33px;height:33px;border-radius:50%;background:#fff}
/* headings */
.slide-title{position:absolute;font-weight:900;font-size:36px;color:var(--ink)}
.chart-title{position:absolute;left:23px;top:24px;font-size:24px;font-weight:700;color:var(--green)}
/* intro */
.intro .photo{left:0;top:0;width:476px;height:623px;background:linear-gradient(135deg,#3d4a55,#8f9aa1 45%,#5a4c3c);border-right:4px solid var(--green)}
.intro .slide-title{left:540px;top:114px;font-size:40px}
.intro-copy{position:absolute;left:540px;top:174px;width:520px;font-size:13.5px;line-height:26px;color:var(--body)}
.intro-copy p+p{margin-top:12px}
/* services */
.services .slide-title{left:28px;top:18px;font-size:40px}
.service-card{position:absolute;width:338px;height:224px;background:#fff;border-radius:6px;box-shadow:0 0 14px rgba(0,0,0,.08);padding:22px 22px}
.service-card svg{width:52px;height:44px;stroke:var(--green);fill:none;stroke-width:2}
.service-card h3{font-size:18px;font-weight:700;margin-top:16px;color:var(--ink)}
.service-card p{font-size:11.5px;line-height:19px;color:var(--body);margin-top:6px}
/* disclaimer */
.disclaimer{background:linear-gradient(180deg,#fafafa,#f0f2f2 60%,#f7f7f7)}
.disclaimer .slide-title{left:23px;top:18px;font-size:30px}
.disclaimer-copy{position:absolute;left:35px;top:120px;width:1034px;font-size:16.6px;line-height:28.3px;color:#555;text-align:justify}
</style>
</head>
<body>

<!-- Cover -->
<section class="slide cover" style="top:50px">
  <div class="photo" role="img" aria-label="Photo of a glass office tower seen from below, in grey tones"></div>
  <div class="hero-brand"><div class="brand-square"></div><div class="brand-name">TESSERA</div></div>
  <div class="cover-band">
    <div class="headline">INDEPENDENT FINANCIAL ADVISORY SERVICES TAILORED TO YOUR GOALS</div>
    <div class="sub">ABC, XYZ – APRIL 2021</div>
  </div>
</section>

<!-- Growth chart -->
<section class="slide framed chart" style="top:767px">
  <h2 class="chart-title">ABC, XYZ – GROWTH OF $1,000 VS BENCHMARK*</h2>
  <div class="brand corner"><div class="brand-square"></div><div class="brand-name">TESSERA</div></div>
  <svg width="1108" height="623" style="position:absolute;left:0;top:0" font-family="Roboto, Arial, sans-serif">
    <g stroke="#c8c8c8" stroke-width="1">
      <line x1="90" y1="117" x2="1010" y2="117"/><line x1="90" y1="181" x2="1010" y2="181"/>
      <line x1="90" y1="246" x2="1010" y2="246"/><line x1="90" y1="310" x2="1010" y2="310"/>
      <line x1="90" y1="374" x2="1010" y2="374"/><line x1="90" y1="438" x2="1010" y2="438"/>
      <line x1="90" y1="503" x2="1010" y2="503"/>
    </g>
    <line x1="90" y1="110" x2="90" y2="567" stroke="#999"/>
    <line x1="90" y1="567" x2="1010" y2="567" stroke="#999"/>
    <g font-size="11" fill="#333" text-anchor="end">
      <text x="76" y="121">$3,500-</text><text x="76" y="185">$3,000-</text><text x="76" y="250">$2,500</text>
      <text x="76" y="314">$2,000</text><text x="76" y="378">$1,500-</text><text x="76" y="442">$1000-</text>
      <text x="76" y="507">$500-</text><text x="76" y="571">$-</text>
    </g>
    <g font-size="9" font-weight="700" fill="#333" text-anchor="end">
      <text transform="translate(116,577) rotate(-90)">Dec-10</text><text transform="translate(144,577) rotate(-90)">Apr-11</text>
      <text transform="translate(172,577) rotate(-90)">Aug-11</text><text transform="translate(200,577) rotate(-90)">Dec-11</text>
      <text transform="translate(228,577) rotate(-90)">Apr-12</text><text transform="translate(256,577) rotate(-90)">Aug-12</text>
      <text transform="translate(284,577) rotate(-90)">Dec-12</text><text transform="translate(312,577) rotate(-90)">Apr-13</text>
      <text transform="translate(340,577) rotate(-90)">Aug-13</text><text transform="translate(368,577) rotate(-90)">Dec-13</text>
      <text transform="translate(396,577) rotate(-90)">Apr-14</text><text transform="translate(424,577) rotate(-90)">Aug-14</text>
      <text transform="translate(452,577) rotate(-90)">Dec-14</text><text transform="translate(480,577) rotate(-90)">Apr-15</text>
      <text transform="translate(508,577) rotate(-90)">Aug-15</text><text transform="translate(536,577) rotate(-90)">Dec-15</text>
      <text transform="translate(564,577) rotate(-90)">Apr-16</text><text transform="translate(592,577) rotate(-90)">Aug-16</text>
      <text transform="translate(620,577) rotate(-90)">Dec-16</text><text transform="translate(648,577) rotate(-90)">Apr-17</text>
      <text transform="translate(676,577) rotate(-90)">Aug-17</text><text transform="translate(704,577) rotate(-90)">Dec-17</text>
      <text transform="translate(732,577) rotate(-90)">Apr-18</text><text transform="translate(760,577) rotate(-90)">Aug-18</text>
      <text transform="translate(788,577) rotate(-90)">Dec-18</text><text transform="translate(816,577) rotate(-90)">Apr-19</text>
      <text transform="translate(844,577) rotate(-90)">Aug-19</text><text transform="translate(872,577) rotate(-90)">Dec-19</text>
      <text transform="translate(900,577) rotate(-90)">Apr-20</text><text transform="translate(928,577) rotate(-90)">Aug-20</text>
    </g>
    <g fill="none" stroke-width="2.4" stroke-linejoin="round">
      <polyline stroke="#a7a7a7" points="97,438.4 146,434.5 195,428.1 244,421.7 293,412.7 342,402.4 391,393.4 440,384.4 489,371.5 538,358.7 587,345.8 636,335.5 685,322.7 734,309.8 783,290.5 832,264.8 881,232.6 906,200 932,151.9"/>
      <polyline stroke="#f6b90f" points="97,438.4 146,435.8 195,429.4 244,424.3 293,415.3 342,403.7 391,396 440,388.2 489,380.5 538,374 587,366.4 636,356.1 685,344.5 734,335.5 783,322.7 832,309.8 881,290.5 932,241.6"/>
      <polyline stroke="#2f55b5" points="97,438.4 146,437.1 160,446 195,430.7 244,425.5 293,416.5 342,406.3 391,396 440,389.5 460,395 489,389.5 538,380.5 587,370.2 636,358.7 685,348.4 710,360 734,354.8 783,329.1 820,345 832,342 850,372 881,297 910,292 932,281.8"/>
      <polyline stroke="#e5632a" points="97,438.4 146,437.1 195,430.7 244,426.8 293,419.1 342,408.8 391,410.1 440,412.7 489,411.4 538,405 587,397.2 636,387 685,380.5 734,374 783,367.7 832,354.8 881,342 920,313.5 932,313.5"/>
    </g>
    <g font-size="13" fill="#333" text-anchor="end">
      <text x="930" y="134">ABC $3,228</text>
      <text x="930" y="243">Hedge Funds 50/50</text><text x="900" y="261">$2,530</text>
      <text x="922" y="290">Benchmark $2,218</text>
      <text x="922" y="389">XYZ $1,971</text>
    </g>
  </svg>
  <div class="page-num"><span class="num">02</span><span class="dot"></span></div>
</section>

<!-- Intro -->
<section class="slide framed intro" style="top:1481px">
  <div class="photo" role="img" aria-label="Photo of an advisor at a laptop showing a line chart"></div>
  <div class="brand corner"><div class="brand-square"></div><div class="brand-name">TESSERA</div></div>
  <h2 class="slide-title">INTRO</h2>
  <div class="intro-copy">
    <p>Lorem ipsum dolor sit amet, consectetur adipiscing elit, sed do eiusmod tempor incididunt ut labore et dolore magna aliqua. Quis ipsu gravida. Risus commodo viverra maecenas accumsan lacus vel fac dolor sit amet, consectetur adipiscing elit, sed do eiusmod tempor incididunt ut labore et dolore ma aliqua. Quis ipsum susse ultrices gravida. Risus commodo viverra maecenas an lacus vel facilisis. Lorem ipsum dolor sit amet, consectetur adig elit, sed do eid tempor incididunt ut labore et dolore magna aliqua.</p>
    <p>Lorem ipsum dolor sit amet, consectetur adipiscing elit, sed do eiusmod tempor incididunt ut labore et dolore magna aliqua. Quis ipsu gravida. Risus commodo viverra maecenas accumsan lacus vel fac dolor sit amet, consectetur adipiscing elit, sed do eiusmod tempor incididunt ut labore et dolore ma aliqua. Quis ipsum susse ultrices gravida.</p>
  </div>
  <div class="page-num"><span class="num">03</span><span class="dot"></span></div>
</section>

<!-- Services -->
<section class="slide framed services" style="top:2197px">
  <h2 class="slide-title">OUR SERVICES</h2>
  <div class="brand corner"><div class="brand-square"></div><div class="brand-name">TESSERA</div></div>

  <article class="service-card" style="left:23px;top:109px">
    <svg viewBox="0 0 52 44"><circle cx="14" cy="12" r="6"/><circle cx="36" cy="12" r="6"/><path d="M3 36c0-8 5-13 11-13s11 5 11 13zM25 36c0-8 5-13 11-13s11 5 11 13z"/></svg>
    <h3>FAMILY OFFICE</h3>
    <p>Lorem ipsum dolor sit amet, consectetur adipiscing elit, sed do eiusmod tempor incididunt ut lab dolore magna aliqua. Quis ipsum suspendisse ultrices gravida. Risus commodo viverra maecenas accumsan lus vel facilisis. Lorem ipsum dolor sit amet,</p>
  </article>
  <article class="service-card" style="left:384px;top:109px">
    <svg viewBox="0 0 52 44"><circle cx="26" cy="22" r="9"/><path d="M26 4v6M26 34v6M8 22h6M38 22h6M13 9l5 5M39 9l-5 5M13 35l5-5M39 35l-5-5"/></svg>
    <h3>ALTERNATIVE INVESTMENTS</h3>
    <p>Lorem ipsum dolor sit amet, consectetur adipiscing elit, sed do eiusmod tempor incididunt ut lab dolore magna aliqua. Quis ipsum suspendisse ultrices gravida. Risus commodo viverra maecenas accumsan lus vel facilisis. Lorem ipsum dolor sit amet,</p>
  </article>
  <article class="service-card" style="left:744px;top:109px">
    <svg viewBox="0 0 52 44"><path d="M4 30h10l10 6h16l8-6M14 30v10M26 26V10M26 18c-6 0-9-4-9-8 6 0 9 4 9 8zM26 14c0-5 4-9 10-9 0 5-4 9-10 9z"/></svg>
    <h3>INVESTMENT MANAGEMENT</h3>
    <p>Lorem ipsum dolor sit amet, consectetur adipiscing elit, sed do eiusmod tempor incididunt ut lab dolore magna aliqua. Quis ipsum suspendisse ultrices gravida. Risus commodo viverra maecenas accumsan lus vel facilisis. Lorem ipsum dolor sit amet,</p>
  </article>
  <article class="service-card" style="left:202px;top:352px">
    <svg viewBox="0 0 52 44"><path d="M10 4h24l8 8v28H10zM34 4v8h8M16 18h14M16 24h20M16 30h10"/><circle cx="34" cy="32" r="5"/></svg>
    <h3>FINANCIAL PLANNING</h3>
    <p>Lorem ipsum dolor sit amet, consectetur adipiscing elit, sed do eiusmod tempor incididunt ut lab dolore magna aliqua. Quis ipsum suspendisse ultrices gravida. Risus commodo viverra maecenas accumsan lus vel facilisis. Lorem ipsum dolor sit amet,</p>
  </article>
  <article class="service-card" style="left:562px;top:352px">
    <svg viewBox="0 0 52 44"><rect x="20" y="2" width="14" height="9"/><circle cx="22" cy="18" r="5"/><path d="M12 40V30c0-4 4-7 10-7s8 3 8 7M8 32h36M14 32v10M38 32v10"/></svg>
    <h3>CONSULTING</h3>
    <p>Lorem ipsum dolor sit amet, consectetur adipiscing elit, sed do eiusmod tempor incididunt ut lab dolore magna aliqua. Quis ipsum suspendisse ultrices gravida. Risus commodo viverra maecenas accumsan lus vel facilisis. Lorem ipsum dolor sit amet,</p>
  </article>
  <div class="page-num"><span class="num">04</span><span class="dot"></span></div>
</section>

<!-- Disclaimer -->
<section class="slide framed disclaimer" style="top:2912px">
  <h2 class="slide-title">DISCLAIMER</h2>
  <div class="brand corner"><div class="brand-square"></div><div class="brand-name">TESSERA</div></div>
  <p class="disclaimer-copy">Disclaimer: this document is a general communication being provided for informational purposes only. It is educational in nature and not designed to be as advice or a recommendation for any specific investment product, strategy, plan feature or other purpose in any jurisdiction. Any examples used are generic, hypothetical and for illustration purposes only. This material does not contain sufficient information to support an investment decision and it should not be relied upon by you in evaluating the merits of investing in any securities or products. In addition, users should make an independent assessment of the legal, regulatory, tax, credit, and accounting implications and determine, together with their own professional advisers, if any investment mentioned herein is believed to be suitable to their personal goals. Investors should ensure that they obtain all available relevant information before making any investment. Any forecasts, figures, opinions or investment techniques and strategies set out are for information purposes only, based on certain assumptions and current market conditions and are subject to change without prior notice. All information presented herein is considered to be accurate at the time of production, but no warranty of accuracy is given and no liability in respect of any error or omission is accepted. It should be noted that investment involves risks, the value of investments and the income from them may fluctuate in accordance with market conditions and taxation agreements and investors may not get back the full amount invested. Both past performance and yields are not reliable indicators of current and future results.</p>
  <div class="page-num"><span class="num">05</span><span class="dot"></span></div>
</section>

<!-- Closing -->
<section class="slide cover closing" style="top:3627px">
  <div class="photo" role="img" aria-label="Photo of a glass office tower seen from below, in grey tones"></div>
  <div class="hero-brand"><div class="brand-square"></div><div class="brand-name">TESSERA</div></div>
  <div class="closing-band">
    <div class="headline">THANK YOU FOR OUR TIME</div>
    <div class="social"><span></span><span></span><span></span></div>
  </div>
</section>

</body>
</html>
```